Commercial Construction Interior Fitout company needs Logo and Business Cards

We need a logo and business card design. We specialise in Commercial Ceilings, Partitions, Plastering and Carpentry.

Company name: 7QX Commercial Interiors. Would like a professional looking card more than a fancy look. Gloss front preferably black pattern with Fluro Green and white text.

Will need:

Name
Position
Phone
Fax
Email
Postal Address
Web address
Updates

Thank you so much everyone for your efforts and fantastic designs..   If I didn't respond to everyone personally,  my apologises. 

Again, thanks all

R.M                               

Target Market(s)

Existing & New clients in the Construction Industry

Industry/Entity Type

Business

Requirements
Nice to have
• 7QX to be overlapped or made into some sort of Logo

```html
<!DOCTYPE html>
<html lang="en">
<head>
<meta charset="utf-8">
<title>7QX Commercial Interiors – Business Card</title>
<link rel="stylesheet" href="https://fonts.googleapis.com/css2?family=Open+Sans:wght@700;800&display=swap">
<style>
  :root {
    --backdrop: #e4e2df;
    --card-black: #0b0b0b;
    --card-white: #fbfbf9;
    --fluro-green: #6cc644;
    --soft-green: #b9dfa6;
    --ink: #111111;
  }
  * { box-sizing: border-box; margin: 0; padding: 0; }
  html, body {
    width: 1200px;
    height: 865px;
    overflow: hidden;
    background: var(--backdrop);
    font-family: "Open Sans", Arial, sans-serif;
  }
  .sheet {
    width: 1200px;
    height: 865px;
    display: flex;
    align-items: center;
    justify-content: center;
    gap: 40px;
  }
  .card {
    position: relative;
    width: 560px;
    height: 320px;
    border-radius: 4px;
    overflow: hidden;
    box-shadow: 0 6px 18px rgba(0,0,0,0.18);
  }

  /* Front */
  .card-front {
    background: var(--card-black);
    display: flex;
    flex-direction: column;
    align-items: center;
    justify-content: center;
    gap: 10px;
  }
  .brand-mark {
    display: flex;
    align-items: center;
    gap: 18px;
  }
  .brand-dot {
    width: 34px;
    height: 34px;
    border-radius: 50%;
    background: var(--fluro-green);
  }
  .brand-name {
    color: var(--fluro-green);
    font-weight: 800;
    font-size: 84px;
    line-height: 1;
    letter-spacing: -2px;
  }
  .brand-tagline {
    color: var(--fluro-green);
    font-weight: 800;
    font-size: 30px;
    letter-spacing: -0.5px;
  }

  /* Back */
  .card-back {
    background: var(--card-white);
    color: var(--ink);
  }
  .back-watermark {
    position: absolute;
    left: -14px;
    top: 40px;
    color: var(--soft-green);
    font-weight: 800;
    font-size: 230px;
    line-height: 1;
    letter-spacing: -10px;
  }
  .holder {
    position: absolute;
    left: 26px;
    top: 22px;
    font-weight: 800;
    font-size: 21px;
    line-height: 1.15;
    letter-spacing: -0.4px;
  }
  .contact-list {
    position: absolute;
    right: 22px;
    bottom: 22px;
    list-style: none;
    text-align: right;
    font-weight: 800;
    font-size: 21px;
    line-height: 1.22;
    letter-spacing: -0.4px;
  }
  .contact-list li {
    display: flex;
    align-items: center;
    justify-content: flex-end;
    gap: 8px;
  }
  .contact-icon {
    width: 20px;
    height: 20px;
    flex: none;
  }
  .icon-spacer { width: 20px; flex: none; }
</style>
</head>
<body>
<main class="sheet">

  <section class="card card-front" aria-label="Card front">
    <div class="brand-mark">
      <span class="brand-dot"></span>
      <span class="brand-name">7QX</span>
    </div>
    <p class="brand-tagline">Commercial Interiors</p>
  </section>

  <section class="card card-back" aria-label="Card back">
    <div class="back-watermark" aria-hidden="true">7QX</div>
    <div class="holder">
      <p class="holder-name">Daniel Marsh</p>
      <p class="holder-role">Director of Sales</p>
    </div>
    <ul class="contact-list">
      <li>555.210.3847
        <svg class="contact-icon" viewBox="0 0 24 24" aria-label="Phone"><path fill="#6cc644" d="M6.6 10.8a15.1 15.1 0 0 0 6.6 6.6l2.2-2.2c.3-.3.7-.4 1-.2 1.1.4 2.3.6 3.6.6.6 0 1 .4 1 1V20c0 .6-.4 1-1 1A17 17 0 0 1 3 4c0-.6.4-1 1-1h3.5c.6 0 1 .4 1 1 0 1.3.2 2.5.6 3.6.1.3 0 .7-.2 1z"/></svg>
      </li>
      <li>555.210.3848
        <svg class="contact-icon" viewBox="0 0 24 24" aria-label="Fax"><rect x="3" y="3" width="18" height="18" rx="2" fill="none" stroke="#6cc644" stroke-width="2"/><rect x="7" y="6" width="10" height="5" fill="#6cc644"/><rect x="7" y="14" width="10" height="3" fill="#6cc644"/></svg>
      </li>
      <li>danielmarsh@7qx.com
        <svg class="contact-icon" viewBox="0 0 24 24" aria-label="Email"><rect x="2" y="2" width="20" height="20" rx="2" fill="none" stroke="#6cc644" stroke-width="2"/><circle cx="12" cy="12" r="3.2" fill="none" stroke="#6cc644" stroke-width="2"/><path d="M15.2 9v4.2c0 1.5 2.6 1.5 2.6-1.2A5.8 5.8 0 1 0 14.5 17" fill="none" stroke="#6cc644" stroke-width="2"/></svg>
      </li>
      <li>42 Harbour Road
        <svg class="contact-icon" viewBox="0 0 24 24" aria-label="Postal address"><rect x="2" y="5" width="20" height="14" fill="#6cc644"/><path d="M2 5l10 8 10-8" fill="none" stroke="#fbfbf9" stroke-width="2"/></svg>
      </li>
      <li>Easton, Westvale 55210<span class="icon-spacer"></span></li>
      <li>7qxcommercialinteriors.com
        <svg class="contact-icon" viewBox="0 0 24 24" aria-label="Website"><path fill="#6cc644" d="M5 2l14 12h-6.5l3.8 7.5-2.6 1.3L9.9 15.2 5 19.5z"/></svg>
      </li>
    </ul>
  </section>

</main>
</body>
</html>
```